Positive Psychology and Coaching Web Design Project

I am a trained psychologist and need to develop a website for my positive life coaching and positive psychology training business. My business is based on Positive Psychology, which is the science of human performance enhancement, to help people reach their potential and flourish in their lives. I work with both individuals, and groups in both businesses and schools helping people improve and create more positive, authentic and successful lives by enhancing their performance and improving their wellbeing, resilience, happiness and quality of life.
The business name: My company is named after a fruit, the pomegranate, which is a very special super fruit, with health enhancing benefits and it is a symbol for growth and positive relationships. The pomegranate is full of many seeds, which represent potential, possibilities and ideas.
The website should have integrity, be professional, strong, inspiring and authentic.

Target Market(s)

I coach and work with executives, individuals and children one-on-one, and also teach and train groups in both businesses and schools. The website needs to be professional, in order to fit into the corporate world of executive coaching, but also friendly and inspiring to fit in with positive education in schools.

Industry/Entity Type

Life Coaching

Font styles to use
Sans Serif

Requirements
Must have
• Use of my logo, however, it is flexible how it is used, and the designer can choose which version to use. There is a closed pomegranate with leaves, an open pomegranate to show seeds with leaves, and both of these without leaves.
See attached files:
File 1: A.png: preferred version used on back of business card
File 4: B.png: preferred version but not used anywhere yet, but goes nicely with A?
File 3: C.png: open pomegranate with seeds used on text side of business card
File 2: D.png: plain pomegranate, could be used as a bullet point??!

A home page with toggle buttons to go to other pages such as:
Home
About
Individuals & Organisations
Young People & Schools
Resources
Contact
Nice to have
• The pomegranate is full of many seeds, which represent potential, possibilities and ideas. My logo has a version with the closed pomegranate, and one with the open pomegranate revealing the seeds. Both these could be used on the website, perhaps clicking on the closed pomegranate to reveal the seeds??! My business card has the closed pomegranate on the back and the open seed pomegranate on the side with my name and details. I trust the designer to choose professional suitable colours, however, I do like the colours used on my logo and business card and the consistency might be nice, these colours are:
Pomegranate Red Colour C:24.67%, M: 100%, Y: 100%, K: 24.49%;
Green Writing Colour: C: 71.16%, M: 49.66%, Y: 100%, K: 54.04%
Green Leaf Colour: C: 69.18%, M: 47.02%, Y: 100%, K: 48.21%

```html
<!DOCTYPE html>
<html lang="en">
<head>
<meta charset="utf-8">
<title>Seedgrove Consulting – Positive Psychology &amp; Life Coaching</title>
<link href="https://fonts.googleapis.com/css2?family=Mulish:wght@400;600;700;800&display=swap" rel="stylesheet">
<style>
  :root {
    --red: #9b1b1e;
    --olive: #566300;
    --ink: #2b2b2b;
    --text: #555555;
    --page-bg: #ebe9e5;
    --white: #ffffff;
    --rule: #d6d6d6;
    --nav-active: #000000;
  }
  * { box-sizing: border-box; margin: 0; padding: 0; }
  html, body { width: 1043px; height: 1200px; overflow: hidden; }
  body {
    font-family: "Mulish", Arial, sans-serif;
    background: var(--white);
    color: var(--text);
    border-top: 3px solid var(--red);
  }
  .site-header { height: 135px; position: relative; }
  .brand {
    position: absolute; left: 78px; top: 48px;
    display: flex; align-items: center; gap: 10px;
    color: var(--red); font-size: 30px; font-weight: 600; letter-spacing: -0.3px;
  }
  .brand-dot { width: 44px; height: 44px; border-radius: 50%; background: var(--red); }
  .contact-box {
    position: absolute; right: 80px; top: 34px; width: 184px;
    text-align: right; font-size: 13px; font-weight: 700; color: #444; line-height: 20px;
  }
  .contact-box .email { border-top: 1px solid var(--rule); margin-top: 6px; padding-top: 6px; }
  .main-nav { height: 52px; background: var(--red); border-bottom: 1px solid #7c1316; }
  .main-nav ul { list-style: none; display: flex; margin-left: 60px; height: 100%; }
  .main-nav a {
    display: flex; align-items: center; height: 100%; padding: 0 20px;
    color: var(--white); text-decoration: none; font-weight: 700; font-size: 16px;
  }
  .main-nav a.active { background: var(--nav-active); }
  .content-area {
    background: var(--page-bg); height: 870px; padding: 33px 60px 0;
    display: flex; gap: 28px; align-items: flex-start;
  }
  .intro-card { background: var(--white); width: 687px; padding: 26px 31px 39px 30px; }
  .intro-card h1 { color: var(--red); font-size: 23px; line-height: 30px; font-weight: 700; margin-bottom: 12px; }
  .lead { color: var(--ink); font-size: 16px; line-height: 22px; width: 560px; margin-bottom: 16px; }
  .body-copy { font-size: 16px; line-height: 22px; width: 560px; }
  .btn {
    display: flex; align-items: center; justify-content: center;
    width: 160px; height: 40px; background: var(--olive); color: var(--white);
    font-size: 16px; text-decoration: none;
  }
  .intro-card > .btn { margin-top: 26px; }
  .program {
    border-top: 1px solid var(--rule); margin-top: 30px; padding-top: 31px;
    display: flex; align-items: flex-start; width: 624px;
  }
  .program + .program { margin-top: 28px; padding-top: 34px; }
  .program-icon { width: 62px; height: 62px; border-radius: 50%; background: var(--red); flex: none; }
  .program-text { margin-left: 20px; width: 300px; }
  .program-text h2 { color: var(--red); font-size: 21px; line-height: 22px; font-weight: 700; margin-top: 12px; width: 265px; }
  .program-text p { font-size: 16px; line-height: 22px; margin: 12px 0 25px 2px; }
  .program-photo { margin-left: auto; width: 220px; height: 145px; flex: none; }
  .photo-portrait { background: linear-gradient(135deg, #f7d9b8, #e9b88a 60%, #3a2a22); }
  .photo-classroom { background: linear-gradient(135deg, #5b5a60, #b59a74 55%, #7a6f66); }
  .sidebar { display: flex; flex-direction: column; gap: 28px; }
  .special-card { background: var(--white); width: 208px; height: 141px; padding: 20px 21px 0; }
  .special-card h3 { color: var(--red); font-size: 15px; font-weight: 700; padding-bottom: 10px; border-bottom: 1px solid var(--rule); }
  .special-body { display: flex; align-items: center; justify-content: space-between; margin-top: 11px; }
  .special-body p { font-size: 13px; line-height: 18px; color: #444; width: 120px; }
  .site-footer { text-align: center; padding-top: 31px; }
  .footer-nav { display: flex; justify-content: center; font-size: 13.5px; }
  .footer-nav a { color: var(--red); text-decoration: none; }
  .footer-nav .sep { color: var(--red); margin: 0 20px; }
  .footer-note { font-size: 13px; color: #444; margin-top: 20px; }
</style>
</head>
<body>
  <header class="site-header">
    <div class="brand"><span class="brand-dot"></span>Seedgrove Consulting</div>
    <div class="contact-box">
      <div>Call us:<br>1800-555-010</div>
      <div class="email">hello@seedgrove.com.au</div>
    </div>
  </header>

  <nav class="main-nav">
    <ul>
      <li><a class="active" href="#">Home</a></li>
      <li><a href="#">About</a></li>
      <li><a href="#">Individuals &amp; Organisations</a></li>
      <li><a href="#">Young People &amp; Schools</a></li>
      <li><a href="#">Resources</a></li>
      <li><a href="#">Contact</a></li>
    </ul>
  </nav>

  <main class="content-area">
    <section class="intro-card">
      <h1>Positive Psychology &amp; Life Coaching</h1>
      <p class="lead">The science of human performance enhancement, to help people reach their potential and flourish in their lives.</p>
      <p class="body-copy">I work with both individuals, and groups in both businesses and schools helping people improve and create more positive, authentic and successful lives by enhancing their performance and improving their wellbeing, resilience, happiness and quality of life.</p>
      <a class="btn" href="#">Lorem ipsum</a>

      <article class="program">
        <span class="program-icon"></span>
        <div class="program-text">
          <h2>Programs for Individuals and Organisations</h2>
          <p>Lorem ipsum dolor sit amet, consectetur adipiscing elit. Nulla sed ipsum pulvinar.</p>
          <a class="btn" href="#">Lorem ipsum</a>
        </div>
        <div class="program-photo photo-portrait" role="img" aria-label="Portrait of a smiling coach"></div>
      </article>

      <article class="program">
        <span class="program-icon"></span>
        <div class="program-text">
          <h2>Programs for Schools and Young People</h2>
          <p>Lorem ipsum dolor sit amet, consectetur adipiscing elit. Nulla sed ipsum pulvinar.</p>
          <a class="btn" href="#">Lorem ipsum</a>
        </div>
        <div class="program-photo photo-classroom" role="img" aria-label="Students working together at a classroom table with tablets"></div>
      </article>
    </section>

    <aside class="sidebar">
      <div class="special-card">
        <h3>Special Item</h3>
        <div class="special-body">
          <p>Lorem ipsum dolor sit amet, conse adipiscing elit.</p>
          <svg width="26" height="26" viewBox="0 0 26 26" aria-hidden="true"><circle cx="13" cy="13" r="13" fill="var(--olive)"/><path d="M10.5 7.5 L16 13 L10.5 18.5" stroke="#fff" stroke-width="3.2" fill="none" stroke-linecap="round" stroke-linejoin="round"/></svg>
        </div>
      </div>
      <div class="special-card">
        <h3>Special Item</h3>
        <div class="special-body">
          <p>Lorem ipsum dolor sit amet, conse adipiscing elit.</p>
          <svg width="26" height="26" viewBox="0 0 26 26" aria-hidden="true"><circle cx="13" cy="13" r="13" fill="var(--olive)"/><path d="M10.5 7.5 L16 13 L10.5 18.5" stroke="#fff" stroke-width="3.2" fill="none" stroke-linecap="round" stroke-linejoin="round"/></svg>
        </div>
      </div>
      <div class="special-card">
        <h3>Special Item</h3>
        <div class="special-body">
          <p>Lorem ipsum dolor sit amet, conse adipiscing elit.</p>
          <svg width="26" height="26" viewBox="0 0 26 26" aria-hidden="true"><circle cx="13" cy="13" r="13" fill="var(--olive)"/><path d="M10.5 7.5 L16 13 L10.5 18.5" stroke="#fff" stroke-width="3.2" fill="none" stroke-linecap="round" stroke-linejoin="round"/></svg>
        </div>
      </div>
    </aside>
  </main>

  <footer class="site-footer">
    <nav class="footer-nav">
      <a href="#">Home</a><span class="sep">|</span>
      <a href="#">About</a><span class="sep">|</span>
      <a href="#">Individuals &amp; Organisations</a><span class="sep">|</span>
      <a href="#">Young People &amp; Schools</a><span class="sep">|</span>
      <a href="#">Resources</a><span class="sep">|</span>
      <a href="#">Contact</a>
    </nav>
    <p class="footer-note">Lorem ipsum dolor sit amet, consectetur adipiscing elit.</p>
  </footer>
</body>
</html>
```